Marlo Fenwick Design, LLC: Die-Cut/Industrial Architecture Work

I have uploaded an amazing business card design which will be printed on stainless steel (metal). The logo does not need to change nor the card layout except as may be necessary to complete the project I am about to describe. THIS IS A DIE-CUT and STEEL BEAM IMAGERY PROJECT.

I am an architect and much of my work is steel structures. This business card project is focused exclusively taking the card design ("as is") to the next level of incredible by incorporating some type of die-cutting or creative imagery (maybe even abstract) of a steel beam which signifies the type of industrial architecture I do. Ultimately, when someone looks at this business card ... I want the card to have an "industrial" feel and it obvious that I do steel structures.

```html
<!DOCTYPE html>
<html lang="en">
<head>
<meta charset="utf-8">
<title>Marlo Fenwick Design, LLC – Steel Business Card</title>
<link rel="stylesheet" href="https://fonts.googleapis.com/css2?family=Quicksand:wght@500;600;700&display=swap">
<style>
  :root{
    --page:#e9e4dc;
    --steel-light:#f4f4f4;
    --steel-mid:#dcdcdc;
    --steel-dark:#c9c9c9;
    --ink:#141414;
    --rust:#b8400f;
    --beam:#d9761e;
    --beam-deep:#a9521a;
    --cut-edge:#1d1d1d;
  }
  *{box-sizing:border-box;margin:0;padding:0}
  html,body{width:1200px;height:1040px;overflow:hidden;background:var(--page)}
  body{font-family:"Quicksand",sans-serif;color:var(--ink);position:relative}
  .card{
    position:absolute;left:180px;width:840px;height:480px;
    background:
      repeating-linear-gradient(0deg,rgba(255,255,255,.35) 0 1px,rgba(0,0,0,.025) 1px 2px),
      linear-gradient(115deg,var(--steel-mid) 0%,var(--steel-light) 35%,var(--steel-dark) 55%,var(--steel-light) 80%,var(--steel-mid) 100%);
    box-shadow:4px 6px 0 #222, 0 10px 24px rgba(0,0,0,.18);
    overflow:hidden;
  }
  .card--front{top:30px}
  .card--back{top:540px}

  /* plain square die-cut */
  .die-cut{
    position:absolute;width:250px;height:250px;
    border:24px solid var(--page);
    box-shadow:inset 3px 3px 0 var(--cut-edge), 3px 3px 0 var(--cut-edge);
  }
  .card--front .die-cut{right:60px;top:115px}
  .card--back .die-cut{left:60px;top:115px}

  /* front identity */
  .identity{position:absolute;left:60px;top:170px;display:flex;align-items:center;gap:22px}
  .identity__mark{width:58px;height:58px;border:5px solid var(--ink);flex:none}
  .identity__rule{width:2px;height:100px;background:var(--ink);flex:none}
  .identity__name{font-size:28px;font-weight:600;letter-spacing:.5px;line-height:1.25;width:260px}
  .tagline{position:absolute;left:60px;top:310px;font-size:19px;font-weight:700;color:var(--rust);letter-spacing:.3px}

  /* back contact */
  .steel-photo{
    position:absolute;right:0;top:0;width:380px;height:480px;
    background:
      linear-gradient(90deg,rgba(244,244,244,1) 0%,rgba(244,244,244,.85) 40%,rgba(244,244,244,0) 75%),
      linear-gradient(160deg,var(--beam) 0%,var(--beam-deep) 55%,var(--beam) 100%);
  }
  .contact{position:absolute;left:360px;top:145px;font-size:21px;font-weight:600;line-height:1.45}
  .contact__row{display:flex;align-items:center;gap:12px}
  .contact__row svg{width:20px;height:20px;flex:none}
  .contact__rule{width:130px;height:2px;background:var(--ink);margin:12px 0 10px}
  .contact__address{display:flex;gap:12px}
  .contact__address svg{width:20px;height:24px;flex:none;margin-top:4px}
</style>
</head>
<body>

<section class="card card--front" aria-label="Card front">
  <div class="identity">
    <div class="identity__mark"></div>
    <div class="identity__rule"></div>
    <div class="identity__name">Marlo Fenwick Design, LLC</div>
  </div>
  <p class="tagline">Studio For Creative Architectural Thought</p>
  <div class="die-cut" aria-hidden="true"></div>
</section>

<section class="card card--back" aria-label="Card back">
  <div class="steel-photo" role="img" aria-label="Photograph of orange painted steel I-beams and bolted girders, fading into the steel card"></div>
  <div class="die-cut" aria-hidden="true"></div>
  <div class="contact">
    <div class="contact__row">
      <svg viewBox="0 0 24 24"><path fill="#141414" d="M6.6 10.8a15 15 0 0 0 6.6 6.6l2.2-2.2a1 1 0 0 1 1-.25 11.4 11.4 0 0 0 3.6.57 1 1 0 0 1 1 1V20a1 1 0 0 1-1 1A17 17 0 0 1 3 4a1 1 0 0 1 1-1h3.5a1 1 0 0 1 1 1c0 1.25.2 2.45.57 3.57a1 1 0 0 1-.25 1z"/></svg>
      <span>555.014.2290</span>
    </div>
    <div class="contact__row">
      <svg viewBox="0 0 24 24"><rect x="2" y="5" width="20" height="14" fill="#141414"/><path d="M2 5l10 8 10-8" fill="none" stroke="#f4f4f4" stroke-width="1.6"/></svg>
      <span>marlo@marlofenwick.design</span>
    </div>
    <div class="contact__row">
      <svg viewBox="0 0 24 24" fill="none" stroke="#141414" stroke-width="2"><circle cx="12" cy="12" r="9"/><path d="M3 12h18M12 3c3 3 3 15 0 18M12 3c-3 3-3 15 0 18"/></svg>
      <span>www.marlofenwick.design</span>
    </div>
    <div class="contact__rule"></div>
    <div class="contact__address">
      <svg viewBox="0 0 20 24"><path fill="#141414" d="M10 0a8 8 0 0 0-8 8c0 6 8 16 8 16s8-10 8-16a8 8 0 0 0-8-8zm0 11a3 3 0 1 1 0-6 3 3 0 0 1 0 6z"/></svg>
      <span>1480 Harbor Crest Road<br>Suite 412, Larkspur FL 33921</span>
    </div>
  </div>
</section>

</body>
</html>
```